Creative Landscape Architecture Company Needs a Creative Business Card Design

Marsh and Partners, Inc. is a landscape architecture (LA) company started in 1997 in Austin, TX. We work on large commerical projects all around the U.S. and provide land planning, site planning, landscape design and architectural renderings.

We don't want this card to look like a LA firm's business card. We are looking for a business card design that is edgy and cool to reflect the more artistic and creative side of our company. We would like our clients to think "now there's a business card unlike any other LA that I've seen before."

We would like it to be in standard 2"x3.5" format. Double sided. Full color ok. Our company logo is attached. We like the logo but would not be adverse to any variations you would like to make to it. Feel free to change it up. Typically the logo has been a light saturated orange color but its not necessary that you stick with it.

Requirements
Must have
• 1. Company name
2. individuals name
3. email address
4. cell number
5. office number
6. website: www.marshandpartners-demo.net
7. Business address
Nice to have
• Can add (but not necessary)
Personal titles such as "president" or "registered landscape architect"

```html
<!DOCTYPE html>
<html lang="en">
<head>
<meta charset="utf-8">
<title>Marsh and Partners, Inc. – Business Card</title>
<link rel="stylesheet" href="https://fonts.googleapis.com/css2?family=Arimo:wght@400;700&family=Source+Sans+3:wght@400;600;700&display=swap">
<style>
  :root {
    --backdrop: #2b3434;
    --card: #ffffff;
    --ink: #231f20;
    --panel: #231f20;
    --leaf-green: #8dc63f;
    --muted: #333333;
  }
  * { margin: 0; padding: 0; box-sizing: border-box; }
  html, body { width: 987px; height: 1200px; overflow: hidden; }
  body { background: var(--backdrop); position: relative; color: var(--ink); }

  .card {
    position: absolute;
    background: var(--card);
    border-radius: 30px;
    overflow: hidden;
  }
  .card--front { left: 96px; top: 112px; width: 790px; height: 450px; }
  .card--back  { left: 96px; top: 637px; width: 792px; height: 436px; }

  .card__swoosh { position: absolute; inset: 0; width: 100%; height: 100%; }

  .brand-mark {
    position: absolute; left: 31px; top: 95px; width: 168px;
    display: flex; flex-direction: column; align-items: center; gap: 14px;
  }
  .brand-mark__square { width: 120px; height: 120px; background: var(--ink); }
  .brand-mark__name {
    font-family: "Arimo", Arial, sans-serif; font-weight: 700;
    font-size: 15px; letter-spacing: 1px; text-align: center; color: var(--ink);
  }

  .company-name {
    position: absolute; left: 231px; top: 92px;
    font-family: "Arimo", Arial, sans-serif; font-weight: 700;
    font-size: 36px; letter-spacing: 0.5px; color: var(--ink); white-space: nowrap;
  }
  .person { position: absolute; left: 232px; top: 154px; font-family: "Source Sans 3", sans-serif; }
  .person__name { font-size: 26px; font-weight: 600; line-height: 1; }
  .person__name strong { font-size: 30px; font-weight: 700; }
  .person__title { font-size: 19px; color: var(--muted); margin-top: 8px; }

  .contacts {
    position: absolute; left: 232px; top: 238px; list-style: none;
    font-family: "Arimo", Arial, sans-serif; font-size: 20px; color: var(--muted);
  }
  .contacts li { height: 33px; white-space: nowrap; }
  .contacts b { color: var(--ink); }
  .contacts .small { font-size: 18px; }

  .address {
    position: absolute; left: 36px; top: 392px;
    font-family: "Source Sans 3", sans-serif; font-size: 19px; color: var(--muted);
  }

  .back-mark {
    position: absolute; left: 0; right: 0; top: 60px;
    display: flex; flex-direction: column; align-items: center; gap: 26px;
  }
  .back-mark__square { width: 190px; height: 190px; background: var(--ink); }
  .back-mark__name {
    font-family: "Arimo", Arial, sans-serif; font-weight: 700;
    font-size: 30px; letter-spacing: 1px; color: var(--ink);
  }
  .website {
    position: absolute; left: 0; right: 0; top: 372px; text-align: center;
    font-family: "Source Sans 3", sans-serif; font-size: 30px; color: var(--ink);
  }
</style>
</head>
<body>
  <section class="card card--front" aria-label="Business card front">
    <svg class="card__swoosh" viewBox="0 0 790 450" preserveAspectRatio="none" aria-hidden="true">
      <path d="M625 0 C760 70 790 300 625 450 L790 450 L790 0 Z" fill="var(--panel)"/>
      <path d="M726 168 C738 320 640 420 430 450 L612 450 C700 375 736 280 726 168 Z" fill="var(--leaf-green)"/>
    </svg>

    <div class="brand-mark">
      <div class="brand-mark__square"></div>
      <div class="brand-mark__name">MARSH &amp; PARTNERS</div>
    </div>

    <h1 class="company-name">MARSH AND PARTNERS</h1>

    <div class="person">
      <div class="person__name">Your <strong>Name</strong></div>
      <div class="person__title">Designation</div>
    </div>

    <ul class="contacts">
      <li><b>c</b> : 0123-456-789</li>
      <li class="small"><b>t</b> : 512.555.0142</li>
      <li><b>e</b> : info@marshandpartners-demo.net</li>
      <li class="small"><b>w</b> : www.marshandpartners-demo.net</li>
    </ul>

    <p class="address">4410 Cedar Bend Road, C118-220, Austin, Texas 78731</p>
  </section>

  <section class="card card--back" aria-label="Business card back">
    <div class="back-mark">
      <div class="back-mark__square"></div>
      <div class="back-mark__name">MARSH &amp; PARTNERS</div>
    </div>
    <p class="website">www.marshandpartners-demo.net</p>
  </section>
</body>
</html>
```